Modern Retail Coffee Label for established Roastery! 17 years!

We are looking for a Retail Coffee Bag Label... JUST THE LABEL TO GO ON AN EXISTING BAG. Our current label is provided and our Logo.. we have had the same Red Bags FOREVER so we are looking for a label to compliment that tradition and to be placed on the bags we have used for 17 years.

We have a retail line of bags with locally roasted coffee. Our business has been around 17years and is in need of a design upgrade! We have a red coffee bag and are looking for a sleek modern label. I will attach a file of our label right now so you can see what it looks like. We are just looking for a more modern version. a few inclusions:

Locally Roasted
100% Arabica Coffee
Heron Kin's Coffee
heronkincoffee.example
logo

The black label with the red and yellow color label is the old one... the new label should be the White background and black border one...

Target Market(s)

Retail Coffee Consumers

Font styles to use
Other font styles liked:
• use what you think. we are located in SW Wisconsin but ship coffee EVERYWHERE

Colors

Designer to choose only greyscale colors for use in the design.

Requirements
Must have
• Locally Roasted (Platteville,WI)
• 100% Arabica Coffee
• heronkincoffee.example
• logo
Nice to have
• Badgers
• "Since 2003"
Should not have
• Any lunabrew or big brand themes

```html
<!DOCTYPE html>
<html lang="en">
<head>
<meta charset="utf-8">
<title>Heron Kin's Coffee – Retail Bag Label</title>
<link href="https://fonts.googleapis.com/css2?family=Montserrat:wght@700;800&family=Lato:wght@400;700&family=Fira+Sans+Condensed:wght@700&display=swap" rel="stylesheet">
<style>
  :root {
    --ink: #1c1a1a;
    --paper: #ffffff;
    --backdrop: #ffffff;
    --band-grey: #c4c4c4;
    --cup-grey: #c2c2c2;
    --steam-grey: #e4e4e4;
    --tan: #c9a672;
  }
  * { margin: 0; padding: 0; box-sizing: border-box; }
  html, body { width: 1200px; height: 822px; overflow: hidden; background: var(--backdrop); }
  .canvas { position: relative; width: 1200px; height: 822px; }

  .label {
    position: absolute; left: 304px; top: 36px;
    width: 592px; height: 750px;
    background: var(--paper);
    border: 5px solid var(--ink);
  }
  .frame-top {
    position: absolute; left: 14px; top: 13px; width: 555px; height: 406px;
    border: 4px solid var(--ink);
  }
  .frame-bottom {
    position: absolute; left: 14px; top: 583px; width: 555px; height: 145px;
    border: 4px solid var(--ink);
  }

  .brand-mark {
    position: absolute; left: 203px; top: 42px; width: 178px; height: 100px;
    border: 4px solid var(--ink); border-radius: 6px; background: var(--paper);
    display: flex; flex-direction: column; align-items: center; justify-content: center;
    font-family: "Montserrat", sans-serif; font-weight: 700; color: var(--ink);
    letter-spacing: 0.5px;
  }
  .brand-mark .mark-line { font-size: 22px; line-height: 1; }
  .brand-mark .mark-rule { width: 152px; height: 2px; background: var(--tan); margin: 10px 0; }

  .cup-art {
    position: absolute; left: 189px; top: 157px; width: 247px; height: 269px;
    background: linear-gradient(to bottom, var(--paper) 0%, var(--steam-grey) 45%, var(--cup-grey) 47%, var(--cup-grey) 100%);
    border-radius: 0 0 80px 80px;
  }

  .kicker {
    position: absolute; left: 0; right: 0; top: 432px; text-align: center;
    font-family: "Montserrat", sans-serif; font-weight: 700; font-size: 42px;
    line-height: 1; color: var(--ink); letter-spacing: 0.5px;
  }
  .headline {
    position: absolute; left: 0; right: 0; top: 470px; text-align: center;
    font-family: "Montserrat", sans-serif; font-weight: 800; font-size: 96px;
    line-height: 1; color: var(--ink); letter-spacing: 1px;
  }
  .roast-band {
    position: absolute; left: 130px; top: 564px; width: 330px; height: 48px;
    background: var(--band-grey); border: 4px solid var(--ink);
    display: flex; align-items: center; justify-content: center;
    font-family: "Lato", sans-serif; font-weight: 700; font-size: 29px;
    color: var(--ink); letter-spacing: 0.5px;
  }
  .origin-claim {
    position: absolute; left: 0; right: 0; top: 630px; text-align: center;
    font-family: "Fira Sans Condensed", sans-serif; font-weight: 700; font-size: 30px;
    line-height: 1; color: var(--ink);
  }
  .web-address {
    position: absolute; left: 0; right: 0; top: 698px; text-align: center;
    font-family: "Lato", sans-serif; font-weight: 400; font-size: 19px;
    line-height: 1; color: var(--ink);
  }
</style>
</head>
<body>
  <main class="canvas">
    <section class="label">
      <div class="frame-top"></div>
      <div class="frame-bottom"></div>

      <div class="brand-mark">
        <span class="mark-line">HERON KIN</span>
        <span class="mark-rule"></span>
        <span class="mark-line">COFFEE</span>
      </div>

      <div class="cup-art" role="img" aria-label="Illustration of a steaming grey coffee cup with the brand's animal emblem on its side"></div>

      <p class="kicker">HERON KIN’S</p>
      <h1 class="headline">COFFEE</h1>
      <div class="roast-band">LOCALLY ROASTED</div>
      <p class="origin-claim">100% Arabica Coffee</p>
      <p class="web-address">heronkincoffee.example</p>
    </section>
  </main>
</body>
</html>
```